Brambel Logging Business Card Design Project

We need a new company business card. We provide professional timber harvesting (logging) and forest management services. I'm open to any creative design. Most company caps and shirts are navy blue and Light grey. Logo does not necessarily have to contain those colors. Logo containing picture of logging equipment, log truck, trees, or logs are acceptable. Be creative. Final logo should communicate our company's pride and professionalism in the East Texas Timber Industry.
Updates

Target Market(s)

Timber owners, sawmills, and forestry professionals

Industry/Entity Type

Business

Requirements
Must have
• Must have Contact Info.
Phone: 936-402-5817
address: PO Box 8462
New Waverly, Tx 77358
www.mbrambellogging.example
mbrambellogging@mailbox.example
Owner: Marv Brambel

Or design must leave room for this info.

```html
<!DOCTYPE html>
<html lang="en">
<head>
<meta charset="utf-8">
<title>Brambel Logging – Business Card</title>
<link rel="stylesheet" href="https://fonts.googleapis.com/css2?family=Exo+2:wght@400;500;700;800&display=swap">
<style>
  :root {
    --page-bg: #d9d9d6;
    --card-white: #ffffff;
    --card-grey: #e9e9e9;
    --brand-yellow: #fbb731;
    --brand-dark: #231f20;
    --text-grey: #5a5a5a;
    --text-light: #ffffff;
  }
  * { box-sizing: border-box; margin: 0; padding: 0; }
  html, body {
    width: 1200px; height: 869px; overflow: hidden;
    background: var(--page-bg);
    font-family: "Exo 2", Arial, sans-serif;
  }
  .canvas { position: relative; width: 1200px; height: 869px; }

  .card {
    position: absolute; width: 600px; height: 340px; overflow: hidden;
    box-shadow: 0 6px 18px rgba(0,0,0,.25);
  }

  /* Front */
  .card-front {
    left: 90px; top: 70px;
    background: linear-gradient(135deg, var(--card-white) 30%, var(--card-grey));
  }
  .brand { position: absolute; display: flex; align-items: center; }
  .brand-mark {
    border-radius: 50%; background: var(--brand-yellow); flex: none;
  }
  .brand-name {
    color: var(--text-grey); font-weight: 800; line-height: 1.05;
  }
  .card-front .brand { left: 120px; top: 118px; gap: 26px; }
  .card-front .brand-mark { width: 100px; height: 100px; }
  .card-front .brand-name { font-size: 38px; }

  /* Back */
  .card-back { left: 520px; top: 470px; background: var(--card-white); }
  .back-art { position: absolute; inset: 0; }
  .card-back .brand { left: 40px; top: 26px; gap: 18px; }
  .card-back .brand-mark { width: 72px; height: 72px; }
  .card-back .brand-name { font-size: 28px; }

  .address {
    position: absolute; left: 88px; top: 126px; width: 320px;
    color: var(--text-light); font-size: 15px; font-weight: 500;
    white-space: nowrap;
  }
  .holder { position: absolute; right: 26px; top: 118px; text-align: right; }
  .holder-name { font-size: 23px; font-weight: 500; color: var(--brand-dark); letter-spacing: 1px; }
  .holder-role { font-size: 11px; color: var(--brand-dark); letter-spacing: 1px; }

  .contact { position: absolute; list-style: none; }
  .contact li {
    display: flex; align-items: center; gap: 12px;
    font-size: 15px; color: var(--brand-dark); height: 36px;
  }
  .contact svg { width: 24px; height: 24px; flex: none; }
  .contact-left { left: 28px; top: 180px; }
  .contact-right { left: 400px; top: 196px; }
  .contact-right li { font-size: 16px; font-weight: 500; }
</style>
</head>
<body>
<main class="canvas">

  <section class="card card-front" aria-label="Card front">
    <div class="brand">
      <span class="brand-mark"></span>
      <p class="brand-name">Marv Brambel<br>Brambel Logging</p>
    </div>
  </section>

  <section class="card card-back" aria-label="Card back">
    <svg class="back-art" viewBox="0 0 600 340" aria-hidden="true">
      <defs>
        <linearGradient id="topShade" x1="0" y1="0" x2="1" y2="1">
          <stop offset="0" stop-color="#d8d8d8"/>
          <stop offset=".5" stop-color="#ffffff"/>
          <stop offset="1" stop-color="#f2f2f2"/>
        </linearGradient>
      </defs>
      <rect width="600" height="340" fill="url(#topShade)"/>
      <path d="M0 120 H440 L420 180 H600 V300 H0 Z" fill="var(--brand-yellow)"/>
      <path d="M60 112 H420 L430 122 V150 L410 178 L400 150 H60 Z" fill="var(--brand-dark)"/>
      <path d="M420 112 L430 122 L420 122 Z" fill="#000"/>
      <rect y="300" width="600" height="40" fill="var(--brand-dark)"/>
    </svg>

    <div class="brand">
      <span class="brand-mark"></span>
      <p class="brand-name">Marv Brambel<br>Brambel Logging</p>
    </div>

    <p class="address">412, 9th floor, Pine Hollow Road NWV</p>

    <div class="holder">
      <p class="holder-name">DALE HOLLIS</p>
      <p class="holder-role">GENERAL MANAGER</p>
    </div>

    <ul class="contact contact-left">
      <li>
        <svg viewBox="0 0 24 24" aria-hidden="true"><rect width="24" height="24" rx="3" fill="var(--brand-dark)"/><circle cx="12" cy="12" r="6.5" fill="none" stroke="var(--brand-yellow)" stroke-width="1.5"/><ellipse cx="12" cy="12" rx="2.8" ry="6.5" fill="none" stroke="var(--brand-yellow)" stroke-width="1.2"/><path d="M5.5 12 H18.5" stroke="var(--brand-yellow)" stroke-width="1.2"/></svg>
        www.yoursitename.example
      </li>
      <li>
        <svg viewBox="0 0 24 24" aria-hidden="true"><rect width="24" height="24" rx="3" fill="var(--brand-dark)"/><rect x="5" y="7" width="14" height="10" fill="none" stroke="var(--brand-yellow)" stroke-width="1.5"/><path d="M5 7 L12 13 L19 7" fill="none" stroke="var(--brand-yellow)" stroke-width="1.5"/></svg>
        yourname@mail.example
      </li>
    </ul>

    <ul class="contact contact-right">
      <li>
        <svg viewBox="0 0 24 24" aria-hidden="true"><rect width="24" height="24" rx="3" fill="var(--brand-dark)"/><path d="M9 6 L11 9 L9.5 10.5 C10.3 12.3 11.7 13.7 13.5 14.5 L15 13 L18 15 L16.5 18 C11 17.5 6.5 13 6 7.5 Z" fill="var(--brand-yellow)"/></svg>
        012 555 0189
      </li>
      <li>
        <svg viewBox="0 0 24 24" aria-hidden="true"><rect width="24" height="24" rx="3" fill="var(--brand-dark)"/><rect x="8" y="5" width="8" height="14" rx="1.5" fill="none" stroke="var(--brand-yellow)" stroke-width="1.5"/><circle cx="12" cy="16.5" r="1" fill="var(--brand-yellow)"/></svg>
        012 555 0189
      </li>
    </ul>
  </section>

</main>
</body>
</html>
```